Label Design - Hair & Beauty Care Wholesaler

Design a label for our client that demonstrates your design skills, your eye for detail and your ability to respond well to the type of brief we produce.

We are offering one prize for the winning design and two participation prizes. The winner will also receive 20 laminated polypropylene labels from the first production run for their portfolio.

Note: This is a test project for us and we know there is a lot of talent out there! Even if you don't win this time, we may be able to engage you for other projects, so if you have the skills and interest we would encourage you to submit a design to make sure we know about you.

One submission only per designer only please.

PROJECT

Our client runs a successful, long-established wholesale hair and beauty care business. Among other things, they sell products like shampoos and conditioners in bulk-buy containers, which hairdressers buy to use in-store in their salons.

(Depending on where you are, the type of product our client needs labels for may be known as a “store brand”, “house brand”, “private label brand”, “own brand”, “home brand” or “generic brand”.)

For this project, the content for the first label to be produced is attached. Keep in mind we will need to be able to change the product name, volume/quantity and ingredients for other labels in future.

Ask questions if you need to! Thanks for participating.

Target Market(s)

Hairdressers and beauty salon owners in Australia.

Industry/Entity Type

Business

Requirements
Must have
• Client's existing logo
All text in the attached "Content" file
Rectangular shape with rounded corners
Finished size 75mm width x 145mm height

```html
<!DOCTYPE html>
<html lang="en">
<head>
<meta charset="utf-8">
<title>Lanolin Shampoo Label</title>
<link rel="stylesheet" href="https://fonts.googleapis.com/css2?family=Cinzel:wght@400;500&family=EB+Garamond:ital,wght@0,400;1,400&display=swap">
<style>
  :root {
    --page: #ffffff;
    --paper: #f4f1ea;
    --paper-edge: #e4dfd4;
    --ink: #3a3631;
    --ink-soft: #5a554d;
    --rule: #8c867b;
    --brand-red: #c0272d;
    --brand-tab: #ece9e2;
    --art-top: #d9d4ca;
    --art-bottom: #a9c98a;
  }
  * { box-sizing: border-box; margin: 0; padding: 0; }
  html, body {
    width: 1200px; height: 850px; overflow: hidden;
    background: var(--page);
  }
  .canvas {
    position: relative; width: 1200px; height: 850px;
    display: flex; align-items: center; justify-content: center;
  }
  .label {
    position: relative; width: 400px; height: 792px;
    background: var(--paper);
    border-radius: 22px;
    box-shadow: 0 0 0 1px var(--paper-edge), 0 4px 10px rgba(0,0,0,0.12);
    overflow: hidden;
    color: var(--ink);
  }
  .label__frame {
    position: absolute; inset: 11px;
    border: 1px solid var(--rule);
    border-radius: 14px;
  }
  .label__art {
    position: absolute; left: 128px; top: 70px; width: 190px; height: 176px;
    background: linear-gradient(to bottom, var(--art-top), var(--art-bottom));
    border-radius: 4px;
  }
  .rule {
    position: absolute; left: 52px; right: 52px;
    border-top: 1px solid var(--rule);
  }
  .rule--double { height: 4px; border-bottom: 1px solid var(--rule); }
  .rule--dotted { border-top: 1px dotted var(--rule); }
  .product-name {
    position: absolute; left: 0; right: 0; top: 298px;
    text-align: center;
    font-family: "Cinzel", serif; font-weight: 400;
    font-size: 46px; letter-spacing: 4px; line-height: 1;
  }
  .product-type {
    position: absolute; left: 0; right: 0; top: 354px;
    text-align: center;
    font-family: "Cinzel", serif; font-size: 21px;
    letter-spacing: 6px; line-height: 1;
  }
  .ingredients {
    position: absolute; left: 60px; right: 60px; top: 418px;
    text-align: center;
    font-family: "EB Garamond", serif; font-style: italic;
    font-size: 15px; line-height: 1.22; color: var(--ink-soft);
  }
  .website {
    position: absolute; left: 0; right: 0; top: 582px;
    text-align: center;
    font-family: "EB Garamond", serif; font-style: italic;
    font-size: 13.5px; color: var(--ink-soft);
  }
  .address {
    position: absolute; left: 40px; width: 160px; top: 640px;
    text-align: right; font-style: normal;
    font-family: "EB Garamond", serif;
    font-size: 13.5px; line-height: 1.3; color: var(--ink-soft);
  }
  .volume {
    position: absolute; left: 36px; top: 740px;
    font-family: "EB Garamond", serif; font-size: 20px;
    letter-spacing: 2px; color: var(--ink-soft);
  }
  .brand-tab {
    position: absolute; left: 209px; top: 628px; width: 100px; bottom: 0;
    display: flex; flex-direction: column;
  }
  .brand-tab__name {
    height: 56px; background: var(--brand-tab);
    display: flex; align-items: center; justify-content: center;
    font-family: "Cinzel", serif; font-weight: 500;
    font-size: 14px; letter-spacing: 1px; color: var(--ink);
  }
  .brand-tab__block { flex: 1; background: var(--brand-red); }
</style>
</head>
<body>
<main class="canvas">
  <article class="label">
    <div class="label__frame"></div>
    <div class="label__art" role="img" aria-label="Illustration of a merino sheep standing on a tuft of green grass"></div>

    <div class="rule rule--double" style="top:282px"></div>
    <h1 class="product-name">LANOLIN</h1>
    <p class="product-type">SHAMPOO</p>
    <div class="rule rule--double" style="top:388px"></div>

    <p class="ingredients">Purified Water, Sodium Laureth Sulphate,<br>Sodium Chloride, Cocoamide DEA,<br>Cocoamidopropyl Hydroxysultaine,<br>Panthenol, PEG-20 Lanolin, Disodium<br>EDTA, Sodium Hydroxymethyl Glycinate,<br>Citric Acid, Perfume</p>

    <div class="rule rule--dotted" style="top:572px"></div>
    <p class="website">www.harboursalonwholesale.com.au</p>
    <div class="rule" style="top:610px"></div>

    <address class="address">
      Harbour Salon Wholesale<br>
      Unit 8, 142 Parkside Drive<br>
      Carlingford NSW 2118
    </address>
    <p class="volume">5 L</p>

    <div class="brand-tab">
      <div class="brand-tab__name">HARBOUR</div>
      <div class="brand-tab__block"></div>
    </div>
  </article>
</main>
</body>
</html>
```